Ferncrest Dental, LLC business card project

Business card to be designed with current logo.
Dental office- please keep design of card that looks clean and professional.
Please include the following info:
Ferncrest Dental, LLC
Dr. Lorna Pettigrew
2871 Marlowe Street
Bethlehem, PA 18093
610-555-0193
ferncrestdental.office@examplemail.test
Hello everyone-
Reason: Just got back from overseas- will look at all designs and provide feedback. Thank you!
Reason: Polling my friends for the final selection-
thank you to all those that participated- so many talented designers!

```html
<!DOCTYPE html>
<html lang="en">
<head>
<meta charset="utf-8">
<title>Ferncrest Dental, LLC – Business Card</title>
<link rel="stylesheet" href="https://fonts.googleapis.com/css2?family=Roboto+Slab:wght@400;700;800&display=swap">
<style>
  :root {
    --leaf: #b2d235;
    --fern: #6a9a3a;
    --paper: #ffffff;
    --edge: #6b6b6b;
    --backdrop: #ffffff;
  }
  * { margin: 0; padding: 0; box-sizing: border-box; }
  html, body {
    width: 1200px;
    height: 686px;
    overflow: hidden;
    background: var(--backdrop);
  }
  .card {
    position: relative;
    width: 1200px;
    height: 686px;
    background: var(--paper);
    border: 1px solid var(--edge);
    overflow: hidden;
    font-family: "Roboto Slab", Georgia, serif;
  }
  .brand-name {
    position: absolute;
    left: 78px;
    top: 60px;
    font-size: 64px;
    font-weight: 400;
    line-height: 1;
    color: var(--fern);
    letter-spacing: -0.5px;
    white-space: nowrap;
  }
  .name-band {
    position: absolute;
    left: 607px;
    top: 284px;
    right: 0;
    height: 70px;
    background: var(--leaf);
  }
  .doctor-name {
    position: absolute;
    right: 24px;
    top: 50%;
    transform: translateY(-50%);
    font-size: 42px;
    font-weight: 800;
    color: var(--paper);
    white-space: nowrap;
  }
  .contact {
    position: absolute;
    right: 25px;
    top: 512px;
    text-align: right;
    font-size: 24px;
    line-height: 34px;
    color: var(--fern);
  }
  .contact p { white-space: nowrap; }
  .contact .street { font-weight: 400; letter-spacing: 0.3px; }
  .contact .city,
  .contact .email { font-weight: 700; }
  .contact .phone { font-weight: 400; }
  .accent { color: var(--leaf); }
  .corner-arc {
    position: absolute;
    left: 0;
    bottom: 0;
  }
</style>
</head>
<body>
  <main class="card">
    <h1 class="brand-name">Ferncrest Dental, LLC</h1>

    <div class="name-band">
      <p class="doctor-name">Dr. Lorna Pettigrew</p>
    </div>

    <address class="contact" style="font-style: normal;">
      <p class="street"><span class="accent">2871</span> MARLOWE STREET</p>
      <p class="city">Bethlehem, <span class="accent">PA 18093</span></p>
      <p class="phone">610-<span class="accent">555</span>-0193</p>
      <p class="email">ferncrestdental.office@examplemail.test</p>
    </address>

    <svg class="corner-arc" width="200" height="150" viewBox="0 536 200 150" aria-hidden="true">
      <path d="M0 547 Q120 598 192 686" fill="none" stroke="var(--leaf)" stroke-width="3"/>
    </svg>
  </main>
</body>
</html>
```